Buch-/eBook-Cover zum Thema Geldmanagement
Zielgruppe
ich benötige ein Buch-Cover (Vorder- und Rückseite) für das Buch Der Pfad der klaren Vermögensführung. Untertitel ist Innere Ruhe und Wohlstand vereint. Das genaue Format ist im Briefing hinterlegt
Aufgabenstellung
Schön wäre es, wenn das Cover hell gehalten wäre. Es soll hochwertig aussehen. Ich habe zwar eigenes Bild-Material angegeben, es können jedoch auch andere Vorschläge kommen.

```html
<!DOCTYPE html>
<html lang="de">
<head>
<meta charset="utf-8">
<title>Der Pfad der klaren Vermögensführung – Umschlag</title>
<link rel="stylesheet" href="https://fonts.googleapis.com/css2?family=Noto+Serif:wght@400;700&family=Gelasio:wght@400&family=Arimo:wght@700&display=swap">
<style>
  :root {
    --teal: #17928a;
    --gold: #d6ad6c;
    --bleed-top: #e5e5e5;
    --bleed-bottom: #a8c3bd;
    --panel-top: #ffffff;
    --panel-bottom: #c3e0dc;
    --guide: #2b2bd6;
    --marker: #ffff00;
    --ink: #111111;
  }
  * { margin: 0; padding: 0; box-sizing: border-box; }
  html, body { width: 1200px; height: 904px; overflow: hidden; }
  body {
    position: relative;
    background: linear-gradient(180deg, var(--bleed-top) 0%, var(--bleed-top) 45%, #cfdcd9 75%, var(--bleed-bottom) 100%);
    font-family: "Noto Serif", Georgia, serif;
    color: var(--teal);
  }
  .spine-bleed {
    position: absolute; left: 543px; top: 0; width: 107px; height: 904px;
    background: var(--bleed-top);
  }
  .panel {
    position: absolute; top: 62px; height: 780px;
    background: linear-gradient(180deg, var(--panel-top) 0%, var(--panel-top) 30%, #e6f2f0 60%, var(--panel-bottom) 100%);
  }
  .back-cover { left: 50px; width: 493px; }
  .front-cover { left: 651px; width: 492px; }
  .spine {
    position: absolute; left: 582px; top: 62px; width: 28px; height: 780px;
    background: #ffffff;
  }
  .guide {
    position: absolute; top: 0; height: 904px; width: 0;
    border-left: 1px dashed var(--guide);
  }

  .title { position: absolute; text-align: center; line-height: 1; }
  .title-row { display: flex; justify-content: center; align-items: baseline; gap: 6px; }
  .title .small, .title .big { color: var(--teal); }
  .title .gold { color: var(--gold); display: block; }

  .front-title { left: 0; width: 492px; top: 64px; }
  .front-title .small { font-size: 32px; }
  .front-title .big { font-size: 54px; }
  .front-title .gold { font-size: 49px; margin-top: -4px; letter-spacing: -0.5px; }
  .front-title .row-2 { margin-top: -10px; padding-left: 10px; }

  .back-title { left: 0; width: 493px; top: 76px; }
  .back-title .small { font-size: 22px; }
  .back-title .big { font-size: 40px; }
  .back-title .gold { font-size: 37px; margin-top: -2px; letter-spacing: -0.3px; }
  .back-title .row-2 { margin-top: -8px; }

  .rule { position: absolute; height: 3px; background: var(--teal); border-radius: 2px; }
  .front-rule { left: 88px; width: 317px; top: 226px; }
  .back-rule { left: 67px; width: 366px; top: 224px; }

  .subtitle {
    position: absolute; left: 0; width: 492px; top: 242px;
    text-align: center; font-family: "Gelasio", Georgia, serif; font-size: 22px; line-height: 28px;
  }
  .butterfly-art {
    position: absolute; left: 17px; top: 320px; width: 467px; height: 334px;
  }
  .author {
    position: absolute; left: 0; width: 492px; top: 734px;
    text-align: center; font-weight: 700; font-size: 21px; letter-spacing: 0.3px;
  }

  .blurb {
    position: absolute; left: 0; width: 493px; top: 269px;
    text-align: center; font-family: "Gelasio", Georgia, serif; white-space: nowrap;
    font-size: 18.5px; line-height: 28.7px;
  }
  .barcode-area {
    position: absolute; left: 296px; top: 658px; width: 171px; height: 101px;
    background: var(--marker); color: var(--ink);
    font-family: "Arimo", Arial, sans-serif; font-weight: 700; font-size: 13px; line-height: 17.5px;
    display: flex; align-items: center; justify-content: center; text-align: center;
  }

  .spine-text {
    position: absolute; white-space: nowrap; font-size: 12.5px;
    transform-origin: left top; transform: rotate(-90deg);
  }
  .spine-author { left: 587px; top: 194px; font-weight: 700; font-size: 11.5px; }
  .spine-title { left: 587px; top: 820px; }
  .spine-title .gold { color: var(--gold); }
</style>
</head>
<body>
  <div class="spine-bleed"></div>

  <section class="panel back-cover">
    <div class="title back-title">
      <div class="title-row row-1"><span class="small">Der</span><span class="big">Pfad</span></div>
      <div class="title-row row-2"><span class="small">der</span><span class="big">klaren</span></div>
      <span class="gold">Vermögensführung</span>
    </div>
    <div class="rule back-rule"></div>
    <p class="blurb">Haben Sie sich schon immer gefragt, was<br>es für ein bewusstes Geldmanagement<br>braucht und wie es Ihnen gelingen kann,<br>in den Zustand von Fülle zu kommen?<br>Wussten Sie, dass es eine Verbindung<br>zwischen Geld und Spiritualität gibt?<br>Möchten Sie wissen, wie Sie in den<br>Geldfluss kommen können und auf<br>welche Art und Weise sich Ihr finanzielles<br>Handeln langfristig zum Positiven<br>verändern kann, dann lesen Sie jetzt<br>dieses Buch!</p>
    <div class="barcode-area">Barcode<br>Lage &amp; Größe<br>2.000" x 1.200"<br>(50.80 mm x 30.48 mm)</div>
  </section>

  <div class="spine"></div>
  <span class="spine-text spine-author">Marlene Kovarik</span>
  <span class="spine-text spine-title">Der Pfad der klaren <span class="gold">Vermögensführung</span></span>

  <section class="panel front-cover">
    <div class="title front-title">
      <div class="title-row row-1"><span class="small">Der</span><span class="big">Pfad</span></div>
      <div class="title-row row-2"><span class="small">der</span><span class="big">klaren</span></div>
      <span class="gold">Vermögensführung</span>
    </div>
    <div class="rule front-rule"></div>
    <p class="subtitle">Innere Ruhe und Wohlstand vereint</p>
    <svg class="butterfly-art" viewBox="0 0 467 334" role="img" aria-label="Illustration eines orange-gelben Schmetterlings mit Währungszeichen auf den Flügeln vor einem hellen Türkisschatten">
      <defs>
        <radialGradient id="wingGlow" cx="50%" cy="45%" r="55%">
          <stop offset="0%" stop-color="#f4b43a"/>
          <stop offset="55%" stop-color="#e99a2c"/>
          <stop offset="100%" stop-color="#bfe0de" stop-opacity="0"/>
        </radialGradient>
      </defs>
      <rect x="0" y="0" width="467" height="334" rx="60" fill="url(#wingGlow)" opacity="0.85"/>
    </svg>
    <p class="author">Marlene Kovarik</p>
  </section>

  <div class="guide" style="left:543px"></div>
  <div class="guide" style="left:577px"></div>
  <div class="guide" style="left:616px"></div>
  <div class="guide" style="left:650px"></div>
</body>
</html>
```